TRELLWICK Construction Group business card for distribution

A business card detailing our services, with our phone number and email address.
- Groundworks / Foundations / Drainage
- Landscaping / Hard Landscaping / Patios / Decking
- Fencing
The card should include company logo and be in the same colours.

Target Market(s)
Domestic Houses
Industry/Entity Type
Construction
Contact Information for Business Card
Phone Number - 07931 258 904 / 07713829516. Email address: trellgroup@stonevane-mail.com
Font styles to use
Serif
Sans Serif
Colors
F0912C
F2A743
F7CA91
FBE8D2
FDF5EE
Requirements
Must have
- Contact numbers. Photos of past work. Company Logo

Nice to have
- Company Logo

```html
<!DOCTYPE html>
<html lang="en">
<head>
<meta charset="utf-8">
<title>TRELLWICK Construction Group – Business Card</title>
<link rel="stylesheet" href="https://fonts.googleapis.com/css2?family=Montserrat:wght@600;700&family=Quicksand:wght@500;700&display=swap">
<style>
  :root {
    --page-bg: #2b2b2c;
    --card-dark: #231f20;
    --card-light: #ffffff;
    --orange: #f0912c;
    --orange-deep: #df8220;
    --ink: #2a2a2a;
    --white: #ffffff;
  }
  * { margin: 0; padding: 0; box-sizing: border-box; }
  html, body {
    width: 1200px; height: 900px; overflow: hidden;
    background: var(--page-bg);
  }
  .sheet {
    width: 1200px; height: 900px;
    display: flex; flex-direction: column; align-items: center; justify-content: center;
    gap: 48px;
  }
  .card {
    position: relative;
    width: 660px; height: 378px;
    border-radius: 28px;
    overflow: hidden;
    box-shadow: 0 12px 30px rgba(0,0,0,.45);
  }

  /* Front */
  .card--front { background: var(--card-dark); }
  .front-band { position: absolute; inset: 0; width: 100%; height: 100%; }
  .front-brand {
    position: absolute; top: 62px; right: 56px;
    text-align: right; color: var(--white);
    font-family: "Montserrat", sans-serif; font-weight: 700;
  }
  .front-brand__name { font-size: 46px; letter-spacing: 2px; line-height: 1; }
  .front-brand__sub { font-size: 15px; letter-spacing: 2.4px; margin-top: 10px; }

  /* Back */
  .card--back { background: linear-gradient(120deg, #ffffff 0%, #f4f4f4 55%, #e9e9e9 100%); }
  .contact {
    position: absolute; top: 40px; left: 40px;
    font-family: "Quicksand", sans-serif; font-weight: 500;
    font-size: 17px; color: var(--ink);
    list-style: none;
  }
  .contact__item { display: flex; align-items: center; gap: 10px; margin-bottom: 8px; }
  .contact__icon { width: 18px; height: 18px; flex: none; }
  .back-brand {
    position: absolute; top: 118px; left: 0; right: 0;
    text-align: center; color: var(--card-dark);
    font-family: "Montserrat", sans-serif; font-weight: 700;
  }
  .back-brand__name { font-size: 50px; letter-spacing: 2px; line-height: 1; }
  .back-brand__sub { font-size: 16px; letter-spacing: 2.6px; margin-top: 10px; }
  .services {
    position: absolute; right: 36px; bottom: 46px;
    text-align: right;
    font-family: "Quicksand", sans-serif; font-weight: 500;
    font-size: 16px; color: var(--ink);
    list-style: none;
  }
  .services__title {
    font-family: "Quicksand", sans-serif; font-weight: 700;
    color: var(--orange); font-size: 19px; margin-bottom: 6px; margin-right: 20px;
  }
  .services__item { display: flex; justify-content: flex-end; align-items: center; gap: 10px; line-height: 1.55; }
  .services__dot { width: 9px; height: 9px; border-radius: 50%; background: var(--orange); flex: none; }
</style>
</head>
<body>
<main class="sheet">

  <section class="card card--front" aria-label="Card front">
    <svg class="front-band" viewBox="0 0 660 378" preserveAspectRatio="none" aria-hidden="true">
      <defs>
        <linearGradient id="bandShade" x1="0" y1="0" x2="1" y2="0">
          <stop offset="0" stop-color="var(--orange-deep)"/>
          <stop offset="1" stop-color="var(--orange)"/>
        </linearGradient>
      </defs>
      <polygon points="0,178 70,156 450,302 660,302 660,378 0,378" fill="url(#bandShade)"/>
    </svg>
    <div class="front-brand">
      <div class="front-brand__name">TRELLWICK</div>
      <div class="front-brand__sub">CONSTRUCTION GROUP LTD</div>
    </div>
  </section>

  <section class="card card--back" aria-label="Card back">
    <ul class="contact">
      <li class="contact__item">
        <svg class="contact__icon" viewBox="0 0 24 24" aria-hidden="true"><path fill="var(--orange)" d="M6.6 10.8a15.1 15.1 0 0 0 6.6 6.6l2.2-2.2a1 1 0 0 1 1-.25 11.4 11.4 0 0 0 3.6.57 1 1 0 0 1 1 1V20a1 1 0 0 1-1 1A17 17 0 0 1 3 4a1 1 0 0 1 1-1h3.5a1 1 0 0 1 1 1c0 1.25.2 2.45.57 3.57a1 1 0 0 1-.25 1z"/></svg>
        <span>07931 258 904 / 07713829516</span>
      </li>
      <li class="contact__item">
        <svg class="contact__icon" viewBox="0 0 24 24" aria-hidden="true"><rect x="2" y="5" width="20" height="14" rx="1.5" fill="var(--orange)"/><path d="M3 6l9 7 9-7" fill="none" stroke="#fff" stroke-width="1.8"/></svg>
        <span>trellgroup@stonevane-mail.com</span>
      </li>
    </ul>

    <div class="back-brand">
      <div class="back-brand__name">TRELLWICK</div>
      <div class="back-brand__sub">CONSTRUCTION GROUP LTD</div>
    </div>

    <ul class="services">
      <li class="services__title">Our Services</li>
      <li class="services__item">Groundworks / Foundations / Drainage <span class="services__dot"></span></li>
      <li class="services__item">Landscaping / Hard Landscaping / Patios / Decking <span class="services__dot"></span></li>
      <li class="services__item">Fencing <span class="services__dot"></span></li>
    </ul>
  </section>

</main>
</body>
</html>
```